Harrowgate Estates Business Card for Apartment Buildings

Create business cards for resident managers who run apartment buildings. The audience is the public who are searching for apartment rentals, and current residents who live at the apartment building. Key design element will be incorporating the company logo, however, the logo cannot dominate. The building name and manager name are more important than the logo. Current business card design leaves little room for copy, so we may need to reduce the size on the current card to allow for more space for copy.

Target Market(s)

Adults 18-65 years of age, who are looking for an apartment rental, plus current residents who live at our apartment buildings.

Industry/Entity Type

Property Management

Contact Information for Business Card

A major design element will be use of the company logo. Important property and manager contact information must be part of the design. The size of the logo will need to be reduced to make room for building and manager contact copy.

Font styles to use
Sans Serif

Colors
3176b5
000000
959595
ffffff

Requirements
Must have
• 1) Incorporate the company logo.
• 2) Use the company colors (dark blue, black/grey, over white).
• 3) FEATURE THE BUILDING NAME
• 4) FEATURE THE MANAGER NAME
• 5) The company name is less important than BUILDING and MANAGER
• 6) Manager contact information
• **SEE ATTACHED CREATIVE BRIEF**
Nice to have
• 1) Back of card logo watermark
• 2) Ability to write notes on back of carfd
Should not have
• Avoid letting the company logo dominate the card, the building name and manager are more important than the company logo.

```html
<!DOCTYPE html>
<html lang="en">
<head>
<meta charset="utf-8">
<title>Harrowgate Estates – Resident Manager Business Card</title>
<link href="https://fonts.googleapis.com/css2?family=Lato:wght@400;700;900&display=swap" rel="stylesheet">
<style>
  :root {
    --brand-blue: #3176b5;
    --ink: #1f1f1f;
    --ink-soft: #333333;
    --grey: #959595;
    --rule: #bdbdbd;
    --paper: #ffffff;
    --backdrop: #8d9191;
  }
  * { box-sizing: border-box; margin: 0; padding: 0; }
  html, body { width: 1200px; height: 1000px; overflow: hidden; }
  body {
    background: var(--backdrop);
    font-family: "Lato", Arial, sans-serif;
    position: relative;
  }
  .card {
    position: absolute;
    left: 320px;
    width: 560px;
    height: 320px;
    background: var(--paper);
    overflow: hidden;
    box-shadow: 0 8px 22px rgba(0,0,0,0.35);
  }
  .card--front { top: 150px; }
  .card--back { top: 520px; }

  /* Front */
  .name-band {
    position: absolute; left: 0; top: 0; width: 100%; height: 92px;
    background: var(--ink);
  }
  .manager-name {
    position: absolute; right: 28px; top: 18px;
    color: var(--paper); font-size: 30px; font-weight: 400; letter-spacing: 0.5px;
  }
  .manager-name strong { font-weight: 900; }
  .manager-title {
    position: absolute; right: 28px; top: 58px;
    color: var(--paper); font-size: 15px;
  }
  .front-swoosh { position: absolute; left: 0; top: 92px; }
  .building-name {
    position: absolute; right: 28px; top: 104px;
    color: var(--brand-blue); font-size: 29px; font-weight: 700;
  }
  .address {
    position: absolute; right: 28px; top: 142px; text-align: right;
    color: var(--ink-soft); font-size: 14px; line-height: 17px;
  }
  .contact-list {
    position: absolute; right: 28px; top: 184px; list-style: none; text-align: right;
    color: var(--ink-soft); font-size: 14px; line-height: 19px;
  }
  .contact-list li { display: flex; justify-content: flex-end; align-items: center; gap: 7px; }
  .contact-list svg { width: 12px; height: 12px; fill: var(--brand-blue); }
  .contact-list .gap { margin-top: 16px; }
  .company-name {
    position: absolute; left: 24px; bottom: 26px;
    color: var(--brand-blue); font-size: 17px; font-weight: 900; letter-spacing: 0.3px;
  }

  /* Back */
  .back-header { position: absolute; left: 0; top: 0; width: 100%; height: 100px; }
  .back-company {
    position: absolute; left: 30px; top: 38px;
    display: flex; align-items: center; gap: 8px;
    color: var(--brand-blue); font-size: 17px; font-weight: 900; white-space: nowrap;
  }
  .back-company .dot { width: 12px; height: 12px; border-radius: 50%; background: var(--brand-blue); }
  .back-divider {
    position: absolute; left: 284px; top: 18px; width: 2px; height: 60px; background: var(--brand-blue);
  }
  .back-building {
    position: absolute; left: 308px; top: 20px; color: var(--ink); text-align: left;
  }
  .back-building .title { font-size: 28px; font-weight: 900; line-height: 30px; }
  .back-building .sub { font-size: 14px; font-weight: 700; letter-spacing: 6px; }
  .back-strip { position: absolute; left: 0; top: 88px; }
  .notes-label {
    position: absolute; left: 30px; top: 155px; font-size: 14px; color: var(--ink-soft);
  }
  .notes-lines { position: absolute; left: 30px; top: 120px; width: 500px; }
  .notes-line { height: 27px; border-bottom: 1px solid var(--rule); }
</style>
</head>
<body>

<section class="card card--front" aria-label="Business card front">
  <div class="name-band">
    <h1 class="manager-name"><strong>MARISOL</strong> DELGADO</h1>
    <p class="manager-title">Resident Manager</p>
  </div>

  <svg class="front-swoosh" width="200" height="140" viewBox="0 0 200 140" aria-hidden="true">
    <path d="M0 0 H120 Q150 0 150 30 V95 Q150 125 120 125 H0 Z" fill="var(--brand-blue)"/>
    <circle cx="80" cy="62" r="50" fill="var(--paper)"/>
    <circle cx="80" cy="62" r="42" fill="none" stroke="var(--brand-blue)" stroke-width="3"/>
  </svg>

  <h2 class="building-name">Cedar Court Apartments</h2>
  <p class="address">2485 Linden Avenue<br>Riverside, CA 92501</p>

  <ul class="contact-list">
    <li>555-214-3860
      <svg viewBox="0 0 24 24"><path d="M6.6 10.8a15 15 0 0 0 6.6 6.6l2.2-2.2c.3-.3.7-.4 1-.2 1.1.4 2.3.6 3.6.6.6 0 1 .4 1 1V20c0 .6-.4 1-1 1A17 17 0 0 1 3 4c0-.6.4-1 1-1h3.5c.6 0 1 .4 1 1 0 1.3.2 2.5.6 3.6.1.3 0 .7-.2 1z"/></svg>
    </li>
    <li>555-708-4192
      <svg viewBox="0 0 24 24"><path d="M6 2h9v6H6zM4 9h16a2 2 0 0 1 2 2v9H2v-9a2 2 0 0 1 2-2z"/></svg>
    </li>
    <li>555-390-6475
      <svg viewBox="0 0 24 24"><path d="M7 1h10a2 2 0 0 1 2 2v18a2 2 0 0 1-2 2H7a2 2 0 0 1-2-2V3a2 2 0 0 1 2-2zm0 3v14h10V4z"/></svg>
    </li>
    <li class="gap">marisol@harrowgate.com
      <svg viewBox="0 0 24 24"><path d="M2 5h20v14H2z"/></svg>
    </li>
    <li>www.harrowgateestates.com
      <svg viewBox="0 0 24 24"><circle cx="12" cy="12" r="10"/></svg>
    </li>
  </ul>

  <p class="company-name">HARROWGATE ESTATES</p>
</section>

<section class="card card--back" aria-label="Business card back">
  <div class="back-header">
    <p class="back-company"><span class="dot"></span>HARROWGATE ESTATES</p>
    <div class="back-divider"></div>
    <div class="back-building">
      <p class="title">Cedar Court</p>
      <p class="sub">APARTMENTS</p>
    </div>
  </div>

  <svg class="back-strip" width="560" height="24" viewBox="0 0 560 24" aria-hidden="true">
    <polygon points="30,6 560,6 560,14 40,14" fill="var(--brand-blue)"/>
  </svg>

  <p class="notes-label">Notes:</p>
  <div class="notes-lines" aria-hidden="true">
    <div class="notes-line"></div>
    <div class="notes-line"></div>
    <div class="notes-line"></div>
    <div class="notes-line"></div>
    <div class="notes-line"></div>
    <div class="notes-line"></div>
    <div class="notes-line"></div>
  </div>
</section>

</body>
</html>
```